Business Card for High End Car Audio Company

Need a new bold business cards with our colors (blue, black, white, silver) and logo's. The card needs to have a high end look and would like the logo to be a large focus if possible. I've included old card for reference. The look was a little too simple for us. Needs nice double sided card.

Our company is a high end car audio company that produces subwoofers, speakers, and amplifiers for cars.

Target Market(s)

Car Audio

Industry/Entity Type

Electronic

Contact Information for Business Card

I included old business card for reference. Will need a template so I can use to create several cards for different people and departments.

Font styles to use
Serif
Sans Serif
Script

Colors
0555a3
ffffff
000000
9d9d9d

Requirements
Must have
• Logo, Info, Colors
Nice to have
• Bold and Elegant Design
Should not have
• Should not be plain.

```html
<!DOCTYPE html>
<html lang="en">
<head>
<meta charset="utf-8">
<title>Voltaris Audio — Business Card</title>
<link href="https://fonts.googleapis.com/css2?family=Open+Sans:wght@400;600;700&display=swap" rel="stylesheet">
<style>
  :root{
    --backdrop:#5e4331;
    --card-white:#ffffff;
    --brand-blue:#1f4391;
    --brand-blue-bright:#1c74bb;
    --brand-navy:#213a7c;
    --ink:#2b2b2b;
    --rule:#c9c9c9;
    --silver-light:#d2d4d6;
    --silver-dark:#6f747a;
  }
  *{margin:0;padding:0;box-sizing:border-box}
  html,body{width:1200px;height:1000px;overflow:hidden}
  body{background:var(--backdrop);font-family:"Open Sans",Arial,sans-serif;position:relative}

  .card{position:absolute;left:266px;width:666px;height:397px;overflow:hidden;box-shadow:0 3px 10px rgba(0,0,0,.35)}
  .card--front{top:74px;background:var(--card-white)}
  .card--back{top:534px;background:radial-gradient(ellipse at 25% 45%,#2f7cc0 0%,#1e5aa0 40%,var(--brand-navy) 100%)}

  .watermark{position:absolute;left:0;top:0;width:666px;height:397px}

  .brand{position:absolute;display:flex;align-items:center;gap:14px;font-weight:700;letter-spacing:2px;line-height:1.05}
  .brand__dot{width:46px;height:46px;border-radius:50%;flex:none}
  .brand__name{display:flex;flex-direction:column;align-items:center;font-size:34px}
  .brand--front{right:32px;top:56px;color:var(--brand-blue)}
  .brand--front .brand__dot{background:var(--brand-blue)}
  .brand--back{right:32px;top:280px;color:var(--card-white)}
  .brand--back .brand__dot{background:var(--card-white)}

  .holder{position:absolute;left:33px;top:190px}
  .holder__name{font-size:22px;font-weight:600;color:var(--brand-blue);letter-spacing:.3px}
  .holder__title{font-size:16px;color:var(--ink);margin-top:1px}

  .divider{position:absolute;left:33px;top:260px;width:462px;height:1px;background:var(--rule)}

  .address{position:absolute;left:33px;top:287px;font-size:16px;line-height:21px;color:var(--ink)}

  .contacts{position:absolute;right:32px;top:250px;list-style:none;font-size:16px;color:var(--ink);text-align:right}
  .contacts li{display:flex;justify-content:flex-end;align-items:center;gap:7px;height:24.5px}
  .contacts svg{width:14px;height:14px;fill:var(--brand-blue)}

  .band{position:absolute;left:0;bottom:0;width:666px;height:28px}
</style>
</head>
<body>
  <section class="card card--front" aria-label="Card front">
    <svg class="watermark" viewBox="0 0 666 397" role="img" aria-label="Faint brand watermark">
      <circle cx="164" cy="96" r="200" fill="none" stroke="#000" stroke-opacity=".035" stroke-width="34"/>
    </svg>

    <div class="brand brand--front">
      <span class="brand__dot"></span>
      <span class="brand__name"><span>VOLTARIS</span><span>AUDIO</span></span>
    </div>

    <div class="holder">
      <p class="holder__name">DANIEL MARSH</p>
      <p class="holder__title">Managing Director</p>
    </div>

    <div class="divider"></div>

    <p class="address">Level 14, 8 Harbour Plaza<br>Sydney, 20, New South Wales</p>

    <ul class="contacts">
      <li>+ 000 000 0000
        <svg viewBox="0 0 14 14"><rect x="3.5" y="0.5" width="7" height="13" rx="1.2" fill="none" stroke="#1f4391" stroke-width="1.2"/><rect x="5" y="2.5" width="4" height="5"/></svg></li>
      <li>+ 000 000 0000
        <svg viewBox="0 0 14 14"><path d="M1 5c0-2 3-3 6-3s6 1 6 3v1h-3V5H4v1H1z"/><path d="M3 7h8l1.5 5.5h-11z"/></svg></li>
      <li>info@voltarisaudio.com
        <svg viewBox="0 0 14 14"><rect x="0.5" y="2.5" width="13" height="9"/><path d="M1 3l6 5 6-5" fill="none" stroke="#fff" stroke-width="1"/></svg></li>
      <li>www.voltarisaudio.com
        <svg viewBox="0 0 14 14"><circle cx="7" cy="7" r="6"/><path d="M1 7h12M7 1c-3 3-3 9 0 12M7 1c3 3 3 9 0 12" fill="none" stroke="#fff" stroke-width=".8"/></svg></li>
    </ul>

    <svg class="band" viewBox="0 0 666 28" preserveAspectRatio="none" aria-hidden="true">
      <defs>
        <linearGradient id="band-blue" x1="0" x2="1"><stop offset="0" stop-color="#213a7c"/><stop offset="1" stop-color="#1c74bb"/></linearGradient>
        <linearGradient id="band-silver" x1="0" x2="1"><stop offset="0" stop-color="#d2d4d6"/><stop offset="1" stop-color="#6f747a"/></linearGradient>
      </defs>
      <polygon points="0,0 318,0 290,28 0,28" fill="url(#band-blue)"/>
      <polygon points="332,0 666,0 666,28 304,28" fill="url(#band-silver)"/>
    </svg>
  </section>

  <section class="card card--back" aria-label="Card back">
    <svg class="watermark" viewBox="0 0 666 397" role="img" aria-label="Large faint brand watermark">
      <circle cx="164" cy="170" r="270" fill="none" stroke="#ffffff" stroke-opacity=".12" stroke-width="44"/>
    </svg>

    <div class="brand brand--back">
      <span class="brand__dot"></span>
      <span class="brand__name"><span>VOLTARIS</span><span>AUDIO</span></span>
    </div>
  </section>
</body>
</html>
```